Newspaper Ad for company move to new location

we are moving our facility to a new city and want to make the announcement that we are coming and share some info about our company and the types of jobs we are bringing. The attached document has the type of info we are looking to put in the ad. We want the ad to communicate a family culture and appeal to a rural market for recruiting potential employees. We are a Christian based, family owned company so our ad should reflect our conservative values.

Target Market(s)

Working people in Cedar Springs MI and surrounding 20 mile area

Industry/Entity Type

Manufacture

Font styles to use
Serif

Colors
33a6d7
0393ce

Requirements
Must have
• product photos you can get them at www.trellisform.example

```html
<!DOCTYPE html>
<html lang="en">
<head>
<meta charset="utf-8">
<title>Trellis Form – We are Hiring in Cedar Springs</title>
<link rel="stylesheet" href="https://fonts.googleapis.com/css2?family=Roboto:wght@400;500;700;900&family=Roboto+Slab:wght@400;600;700&family=Tinos:wght@400;700&display=swap">
<style>
  :root {
    --brand-blue: #33a6d7;
    --deep-blue: #0393ce;
    --ink: #1d1d1b;
    --frame: #222222;
    --paper: #ffffff;
    --logo-navy: #1f2a44;
  }
  * { box-sizing: border-box; margin: 0; padding: 0; }
  html, body { width: 927px; height: 1200px; overflow: hidden; background: var(--paper); }
  .ad {
    position: relative;
    width: 927px; height: 1200px;
    background: var(--paper);
    color: var(--ink);
    font-family: "Tinos", "Times New Roman", serif;
  }
  .ad-frame {
    position: absolute; left: 15px; top: 15px; width: 897px; height: 1170px;
    border: 2px solid var(--frame); border-radius: 22px;
  }
  .brand {
    position: absolute; left: 612px; top: 44px; height: 72px;
    display: flex; align-items: center; gap: 12px;
  }
  .brand-square { width: 62px; height: 62px; background: var(--logo-navy); }
  .brand-name {
    font-family: "Roboto", Arial, sans-serif; font-weight: 900; font-size: 34px;
    line-height: 32px; color: var(--logo-navy); letter-spacing: 0.5px;
  }
  .hero-band {
    position: absolute; left: 16px; top: 140px; width: 895px; height: 370px;
    background: var(--brand-blue);
  }
  .hero-intro {
    position: absolute; left: 470px; top: 178px; width: 440px;
    text-align: center; color: var(--paper);
    font-family: "Roboto Slab", Georgia, serif; font-weight: 600; font-size: 33px; line-height: 42px;
  }
  .hero-title {
    position: absolute; left: 430px; top: 268px; width: 480px;
    text-align: center; color: var(--paper);
    font-family: "Roboto", Arial, sans-serif; font-weight: 500; font-size: 134px; line-height: 140px;
    letter-spacing: 2px;
  }
  .product-photo {
    position: absolute; border-radius: 50%; border: 4px solid var(--paper);
  }
  .photo-dips { left: 36px; top: 88px; width: 222px; height: 222px;
    background: radial-gradient(circle at 40% 45%, #d6a12e, #8b3d1e 55%, #c9c4b8); }
  .photo-salad { left: 142px; top: 200px; width: 250px; height: 250px;
    background: radial-gradient(circle at 50% 50%, #7aa83c, #c84a2a 45%, #e9e6dc 80%); }
  .photo-interior { left: 36px; top: 330px; width: 262px; height: 262px;
    background: radial-gradient(circle at 60% 40%, #6a6a6a, #262626 60%, #0e0e0e); }
  .about {
    position: absolute; left: 40px; top: 594px; width: 480px;
    font-size: 17.6px; line-height: 22px;
  }
  .about p + p { margin-top: 22px; }
  .positions-heading {
    position: absolute; left: 560px; top: 462px; width: 320px;
    text-align: center; font-family: "Roboto Slab", Georgia, serif; font-weight: 700;
    font-size: 20px; line-height: 25px;
  }
  .positions { list-style: none; }
  .position-icon { position: absolute; }
  .position {
    position: absolute; left: 582px;
    font-family: "Roboto Slab", Georgia, serif; font-size: 19px; color: var(--brand-blue);
  }
  .position::before {
    content: ""; display: inline-block; width: 7px; height: 7px; border-radius: 50%;
    background: var(--ink); margin-right: 8px; vertical-align: middle; position: relative; top: -2px;
  }
  .offer-heading {
    position: absolute; left: 0; top: 976px; width: 927px; text-align: center;
    font-family: "Roboto", Arial, sans-serif; font-weight: 500; font-size: 36px;
  }
  .offers {
    position: absolute; left: 0; top: 1032px; width: 927px; list-style: none;
    display: flex; justify-content: center; gap: 20px;
    font-family: "Roboto Slab", Georgia, serif; font-size: 19px; color: var(--brand-blue);
  }
  .offers li::before {
    content: ""; display: inline-block; width: 7px; height: 7px; border-radius: 50%;
    background: var(--ink); margin-right: 6px; vertical-align: middle; position: relative; top: -2px;
  }
  .apply {
    position: absolute; left: 90px; top: 1068px; width: 747px; text-align: center;
    font-family: "Roboto", Arial, sans-serif; font-size: 15px; line-height: 20px;
  }
  .contact {
    position: absolute; left: 0; top: 1126px; width: 927px;
    display: flex; justify-content: center; gap: 30px;
    font-family: "Roboto", Arial, sans-serif; font-size: 19px;
  }
</style>
</head>
<body>
<main class="ad">
  <div class="ad-frame"></div>

  <div class="brand">
    <span class="brand-square"></span>
    <span class="brand-name">TRELLIS<br>FORM</span>
  </div>

  <div class="hero-band"></div>
  <div class="product-photo photo-dips" role="img" aria-label="Photo of dip and salsa containers in clear packaging"></div>
  <div class="product-photo photo-salad" role="img" aria-label="Photo of fresh salad and fruit in clear clamshell trays"></div>
  <div class="product-photo photo-interior" role="img" aria-label="Photo of automotive interior trim on a dashboard and console"></div>

  <p class="hero-intro">We are coming to<br>Cedar Springs and we are</p>
  <h1 class="hero-title">HIRING</h1>

  <section class="about">
    <p>We are a family owned company opened in 1967 that has outgrown our Grand Rapids facility. We have purchased the building working on West St. currently housing Birchline Outfitters. We expect to start moving equipment to the new location in November.</p>
    <p>Our products includes packaging for a number of industries including: food, cell phone accessories, hardware, sporting goods, health, beauty and household products. We also produce decorative parts for the interior of automobiles including trim for the dash, doors and center console.</p>
  </section>

  <h2 class="positions-heading">Some positions we are<br>currently hiring :</h2>

  <svg class="position-icon" style="left:690px;top:538px" width="54" height="22" viewBox="0 0 54 22" aria-hidden="true">
    <path d="M2 6 h10 l3 -4 h5 v18 h-5 l-3 -4 h-10 l3 -5z M20 8 h32 v6 h-32z" fill="var(--brand-blue)"/>
  </svg>
  <svg class="position-icon" style="left:694px;top:612px" width="44" height="42" viewBox="0 0 44 42" aria-hidden="true">
    <path d="M4 6 h36 l-4 32 h-28z" fill="none" stroke="var(--brand-blue)" stroke-width="5" stroke-linejoin="round"/>
    <path d="M2 6 h40" stroke="var(--brand-blue)" stroke-width="5"/>
  </svg>
  <svg class="position-icon" style="left:694px;top:700px" width="46" height="52" viewBox="0 0 46 52" aria-hidden="true">
    <rect x="24" y="4" width="18" height="44" fill="#9fd3e8"/>
    <rect x="4" y="30" width="18" height="18" fill="#e0a04a"/>
    <rect x="10" y="16" width="12" height="14" fill="#c77fb0"/>
  </svg>
  <svg class="position-icon" style="left:650px;top:786px" width="124" height="58" viewBox="0 0 124 58" aria-hidden="true">
    <path d="M4 34 L62 4 L120 34" fill="none" stroke="var(--brand-blue)" stroke-width="6"/>
    <rect x="44" y="30" width="22" height="16" fill="var(--brand-blue)"/>
    <path d="M66 34 h8 l6 6 v6 h-14z" fill="var(--brand-blue)"/>
    <circle cx="52" cy="49" r="4" fill="var(--brand-blue)"/>
    <circle cx="74" cy="49" r="4" fill="var(--brand-blue)"/>
  </svg>
  <svg class="position-icon" style="left:696px;top:878px" width="40" height="48" viewBox="0 0 40 48" aria-hidden="true">
    <path d="M4 20 a16 16 0 0 1 32 0z" fill="#1a5fbf"/>
    <path d="M6 20 h28 v10 a14 16 0 0 1 -28 0z" fill="#e2b48f"/>
  </svg>

  <ul class="positions">
    <li class="position" style="top:578px">Mold and Die Makers</li>
    <li class="position" style="top:664px">Thermoforming Technicians</li>
    <li class="position" style="top:758px">Packers</li>
    <li class="position" style="top:843px">Warehouse</li>
    <li class="position" style="top:930px">Trimming Inspectors</li>
  </ul>

  <h2 class="offer-heading">We offer :</h2>
  <ul class="offers">
    <li>Competitive wages</li>
    <li>Benefits</li>
    <li>Paid Vacation</li>
    <li>Paid Personal Time</li>
    <li>401k Plan</li>
  </ul>

  <p class="apply">To apply for a position, send your resume to jobs@trellisform.example or 2280 Orchard Ave. NW Grand Rapids, MI&nbsp; 49500 or stop in to our Orchard location between 8:00 am and 4:30 pm to fill out an application.</p>

  <p class="contact">
    <span>Ph: 555 010-4821</span>
    <span>Web: www.trellisform.example</span>
    <span>Email: jobs@trellisform.example</span>
  </p>
</main>
</body>
</html>
```